Business Card Design for Occupational Medicine Start Up Company

We need to design a professional business card. We are a healthcare company providing occupational medicine services to blue collar industries. We are professional, efficient and high quality service providers.

Target Market(s)

Blue Collar Industry: Shipbuilding, Ports, Trucking Companies; The Executives and Safety Officers for these companies

Industry/Entity Type

Healthcare

Contact Information for Business Card

Logo, Name, Title, Email, Phone

Other font styles liked:
• Please match our Brand Guide

Requirements
Must have
• Our Company Colors and Logo

```html
<!DOCTYPE html>
<html lang="en">
<head>
<meta charset="utf-8">
<title>Harborline Care – Business Card</title>
<link href="https://fonts.googleapis.com/css2?family=Lato:wght@400;700&family=Montserrat:wght@400;700;800&display=swap" rel="stylesheet">
<style>
  :root {
    --backdrop: #1b1b1b;
    --kraft-light: #dfc195;
    --kraft-mid: #c49c68;
    --kraft-dark: #a57748;
    --ink: #111111;
  }
  * { margin: 0; padding: 0; box-sizing: border-box; }
  html, body {
    width: 1093px;
    height: 1200px;
    overflow: hidden;
    background: var(--backdrop);
  }
  .canvas {
    position: relative;
    width: 1093px;
    height: 1200px;
  }
  .card {
    position: absolute;
    left: 264px;
    width: 580px;
    height: 357px;
    background: linear-gradient(135deg, var(--kraft-light) 0%, var(--kraft-mid) 55%, var(--kraft-dark) 100%);
    color: var(--ink);
    text-align: center;
  }
  .card--front { top: 226px; }
  .card--back { top: 620px; }

  .holder {
    position: absolute;
    top: 70px;
    left: 0;
    right: 0;
  }
  .holder__name {
    font-family: "Montserrat", sans-serif;
    font-weight: 800;
    font-size: 21px;
    letter-spacing: 0.2px;
    line-height: 22px;
  }
  .holder__title {
    font-family: "Lato", sans-serif;
    font-size: 16.5px;
    line-height: 18px;
  }
  .rule {
    width: 94px;
    height: 1px;
    margin: 0 auto;
    background: var(--ink);
  }
  .rule--upper { margin-top: 15px; }
  .contact {
    margin-top: 19px;
    font-family: "Lato", sans-serif;
    font-size: 17px;
    line-height: 21px;
  }
  .rule--lower { margin-top: 16px; }
  .address {
    margin-top: 19px;
    font-family: "Lato", sans-serif;
    font-size: 17px;
    line-height: 20.5px;
  }

  .brand {
    position: absolute;
    top: 148px;
    left: 0;
    right: 0;
    display: flex;
    align-items: center;
    justify-content: center;
    gap: 16px;
  }
  .brand__dot {
    width: 40px;
    height: 40px;
    border-radius: 50%;
    background: var(--ink);
  }
  .brand__name {
    font-family: "Montserrat", sans-serif;
    font-weight: 700;
    font-size: 33px;
    letter-spacing: 1px;
    color: var(--ink);
  }
</style>
</head>
<body>
<main class="canvas">
  <section class="card card--front" aria-label="Business card front">
    <div class="holder">
      <h1 class="holder__name">DANIEL REYES</h1>
      <p class="holder__title">Managing Director</p>
      <div class="rule rule--upper"></div>
      <p class="contact">
        M: 055-987 654 321<br>
        E: hello@harborlinecare.com<br>
        W: www.harborlinecare.com
      </p>
      <div class="rule rule--lower"></div>
      <p class="address">
        480, Dockside Avenue<br>
        Portmouth, 204518.
      </p>
    </div>
  </section>

  <section class="card card--back" aria-label="Business card back">
    <div class="brand">
      <span class="brand__dot"></span>
      <span class="brand__name">HARBORLINE CARE</span>
    </div>
  </section>
</main>
</body>
</html>
```